A5 flyer required for 3D printing company

We are a 3D printing company providing our customers with customised 3D printed figurines services. And we need a double sided flyer design for our company, either to display in the shop or hand out on streets. Our website (www.quillpixfigures.com.au) describes what we do and what the products look like.
The final flyer should tell our potential customers the following points:
1. We can make 3D printed figurines in incredible likeness for our customers;
2. Advanced 3D scanning and 3D printing technology;
3. Includes our price table, and grand opening 15% off for all products till 31st May 2016;
full body size Retail
8cm $159
10cm $239
12cm $279
15cm $339
18cm $449
20cm $599
Bust size
8cm $239
10cm $279
12cm $339
4. Use one or more photos supplied to show the final products compared with real person, you can use lasso tools to crop the background if you like;
5. Our contact details;
Address: Suite 7 Level 2, 316 Harlow Street Sydney, in the Pennart Building
Telephone: 02 9475 6302
Email: info@quillpixfigures.com.au
Web: www.quillpixfigures.com.au
The flyer should catch customers' eyes at the first sight because we will be handing out the flyers on streets as well. You can use any material used on our website (www.quillpixfigures.com.au).
We would like to see the design in line with our colour scheme used for our logo. The two colours used in the logo are C70 M0 Y0 K0 and C83 M53 Y6 K0 for your reference. And the font we used in our logo is hobo std for your reference.
If you have any questions about our products or the flyer, please feel free to drop us a message.

```html
<!DOCTYPE html>
<html lang="en">
<head>
<meta charset="utf-8">
<title>QuillPix Figures – A5 Flyer</title>
<link href="https://fonts.googleapis.com/css2?family=Tinos:wght@400;700&display=swap" rel="stylesheet">
<style>
:root{
  --navy:#101a4d;
  --navy-light:#1b2a66;
  --cyan:#29c0ef;
  --blue:#1f6fc0;
  --white:#ffffff;
  --stage:#e9eaee;
  --photo-warm:#d9c7b4;
  --photo-sky:#6f9ccd;
  --photo-land:#8b7a5e;
}
*{box-sizing:border-box;margin:0;padding:0}
html,body{width:1200px;height:900px;overflow:hidden}
body{background:var(--stage);font-family:"Tinos","Times New Roman",serif;color:var(--white);position:relative}
.flyer{position:absolute;width:420px;height:595px;background:var(--navy);overflow:hidden;box-shadow:0 6px 18px rgba(0,0,0,.35)}
.flyer--front{left:150px;top:123px}
.flyer--back{left:633px;top:125px}
.abs{position:absolute}
.photo{position:absolute}
.photo--hero{left:0;top:0;width:420px;height:260px;background:linear-gradient(160deg,#e8ddd1,var(--photo-warm) 55%,#c9a9a3)}
.shape-layer{position:absolute;left:0;top:0;width:420px;height:595px}
.photo-circle{position:absolute;border-radius:50%;border:3px solid var(--white)}
.photo-circle--beach{left:52px;top:201px;width:86px;height:86px;background:linear-gradient(160deg,#8fb6d9,#d8b789)}
.photo-circle--portrait{left:155px;top:193px;width:100px;height:100px;background:linear-gradient(160deg,#9db8d3,#3a3f4a)}
.brand-badge{position:absolute;left:262px;top:130px;width:132px;height:132px;border-radius:50%;background:var(--white);display:flex;align-items:center;justify-content:center;text-align:center}
.brand-name{font-family:"Tinos",serif;font-weight:700;color:var(--blue);font-size:22px;line-height:1.05}
.section-title{font-weight:700;font-size:14px;line-height:1.15}
.rule{border-bottom:1px solid var(--white);padding-bottom:2px}
.body-text{font-size:10px;line-height:1.3}
.about{left:28px;top:300px;width:366px}
.about .section-title{width:122px}
.about .body-text{margin-top:12px}
.materials{left:28px;top:392px;width:366px}
.materials .section-title{width:204px}
.materials .body-text{margin-top:10px;padding-left:2px}
.highlights{position:absolute;left:31px;top:463px;width:358px;height:92px;background:var(--cyan);border-radius:10px;padding:9px 10px 0 10px;color:var(--white)}
.highlights ol{list-style:none;font-weight:700;font-size:11px;line-height:1.3}
.highlights li{padding-left:12px;text-indent:-12px}
.highlights .date{font-size:15px}
.footer-bar{position:absolute;left:0;bottom:0;width:420px;height:30px;background:var(--white);color:var(--navy);display:flex;align-items:center;justify-content:space-around;font-size:10px;padding:0 8px}
.footer-bar span{display:flex;align-items:center;gap:5px}
.icon{width:10px;height:10px;flex:none}
.prices-title{left:33px;top:14px;width:124px;font-size:18px}
.col-head{font-weight:700;font-size:13px}
.full-head{left:34px;top:48px}
.bust-head{left:257px;top:50px}
.divider{left:231px;top:45px;width:1px;height:108px;background:var(--white);opacity:.8}
.pill{position:absolute;width:72px;height:18px;background:var(--cyan);border-radius:4px;font-weight:700;font-size:11px;display:flex;align-items:center;justify-content:center}
.contact-title{left:37px;top:160px;width:124px;font-size:18px}
.contact-intro{left:37px;top:190px;width:172px;font-size:10px;line-height:1.25}
.hours-title{left:37px;top:240px;font-size:11px}
.hours{left:37px;top:258px;font-size:10px;line-height:1.25}
.appointment{left:37px;top:295px;font-size:9.5px}
.contact-list{left:243px;top:184px;width:170px;font-size:10px;line-height:1.25}
.contact-list li{list-style:none;display:flex;gap:8px;margin-bottom:6px}
.contact-list li:first-child{margin-bottom:10px}
.photo--scene{left:0;top:330px;width:420px;height:265px;background:linear-gradient(180deg,#4f86c4,var(--photo-sky) 30%,#a7b1b3 55%,var(--photo-land) 80%,#9a9a96)}
.photo-circle--family{left:90px;top:317px;width:100px;height:100px;background:linear-gradient(170deg,#c9d6e3,#8c7f78)}
</style>
</head>
<body>

<section class="flyer flyer--front">
  <div class="photo photo--hero" role="img" aria-label="Photo of a wedding cake topped with 3D printed bride and groom figurines"></div>
  <svg class="shape-layer" viewBox="0 0 420 595" aria-hidden="true">
    <path d="M0 236 C120 262 300 250 420 150 L420 595 L0 595 Z" fill="var(--white)"/>
    <path d="M0 246 C130 272 310 262 420 162 L420 595 L0 595 Z" fill="var(--cyan)"/>
    <path d="M0 254 C130 280 310 270 420 172 L420 595 L0 595 Z" fill="var(--navy)"/>
    <path d="M0 380 C150 350 300 330 420 300 L420 595 L0 595 Z" fill="var(--navy-light)" opacity=".35"/>
  </svg>
  <div class="photo-circle photo-circle--beach" role="img" aria-label="Photo of a child playing in sand at the beach"></div>
  <div class="photo-circle photo-circle--portrait" role="img" aria-label="Photo of a young man posing beside his figurine"></div>
  <div class="brand-badge"><span class="brand-name">QuillPix<br>Figures</span></div>

  <div class="abs about">
    <h2 class="section-title rule">About us:</h2>
    <p class="body-text">QuillPix Figures was born from the desire to bring memories to life. They offer people the amazing opportunity to relive the most beautiful moments in their lives. We use the most detailed and fast technology capable of collecting 3D data and process it into superb miniature figurines of… you.</p>
  </div>
  <div class="abs materials">
    <h2 class="section-title rule">What are the<br>3D printed figurines made of?</h2>
    <p class="body-text">They’re made out of passion and dedication, and a really cool patent material that looks and feels like plaster, but it’s called DuraCast PX.</p>
  </div>
  <div class="highlights">
    <ol>
      <li>1.We can make 3D printed figurines in incredible likeness for our customers;</li>
      <li>2. Advanced 3D scanning and 3D printing technology;</li>
      <li>3. Includes our price table, and grand opening 15% off for all products till <span class="date">31st May 2016;</span></li>
    </ol>
  </div>
  <footer class="footer-bar">
    <span><svg class="icon" viewBox="0 0 10 10"><path d="M2 1 L4 3 L3 4 Q4 6 6 7 L7 6 L9 8 L8 9 Q3 9 1 2 Z" fill="var(--navy)"/></svg>02 9475 6302</span>
    <span><svg class="icon" viewBox="0 0 10 10"><rect x="0.5" y="2" width="9" height="6" fill="var(--navy)"/><path d="M0.5 2 L5 5.5 L9.5 2" stroke="var(--white)" fill="none" stroke-width=".8"/></svg>info@quillpixfigures.com.au</span>
    <span><svg class="icon" viewBox="0 0 10 10"><circle cx="5" cy="5" r="4.3" fill="none" stroke="var(--navy)"/><ellipse cx="5" cy="5" rx="1.8" ry="4.3" fill="none" stroke="var(--navy)"/><path d="M.7 5 H9.3" stroke="var(--navy)"/></svg>www.quillpixfigures.com.au</span>
  </footer>
</section>

<section class="flyer flyer--back">
  <svg class="shape-layer" viewBox="0 0 420 595" aria-hidden="true">
    <path d="M150 140 C250 60 330 20 420 0 L420 330 L0 330 L0 220 C60 200 110 170 150 140 Z" fill="var(--navy-light)" opacity=".55"/>
  </svg>
  <h2 class="abs section-title rule prices-title">Our prices:</h2>
  <h3 class="abs col-head full-head">FULL BODY SIZERETAIL</h3>
  <div class="abs divider"></div>
  <h3 class="abs col-head bust-head">BUST SIZE</h3>
  <div class="pill" style="left:35px;top:74px">8cm $159</div>
  <div class="pill" style="left:35px;top:99px">10cm$239</div>
  <div class="pill" style="left:35px;top:124px">12cm$279</div>
  <div class="pill" style="left:124px;top:74px">15cm$339</div>
  <div class="pill" style="left:124px;top:99px">18cm$449</div>
  <div class="pill" style="left:124px;top:124px">20cm$599</div>
  <div class="pill" style="left:257px;top:74px">8cm$239</div>
  <div class="pill" style="left:257px;top:99px">10cm$279</div>
  <div class="pill" style="left:257px;top:124px">12cm$339</div>

  <h2 class="abs section-title rule contact-title">Contact us:</h2>
  <p class="abs contact-intro">We are always happy to meet our customers and answer their questions about 3D printed figurines</p>
  <h3 class="abs col-head hours-title">TRADING HOURS:</h3>
  <p class="abs hours">Mon-Fri 10.30am – 7.30pm<br>Saturday 10.00am – 5.00pm</p>
  <p class="abs appointment">Sundays by appointment only</p>

  <ul class="abs contact-list">
    <li><svg class="icon" viewBox="0 0 10 14" style="height:14px"><path d="M5 13 C2 8 1 6.5 1 4.5 A4 4 0 0 1 9 4.5 C9 6.5 8 8 5 13 Z" fill="var(--white)"/><circle cx="5" cy="4.5" r="1.5" fill="var(--navy)"/></svg><span>Suite 7, Level 2,<br>316 Harlow Street,<br>Sydney NSW 2000</span></li>
    <li><svg class="icon" viewBox="0 0 10 10"><path d="M2 1 L4 3 L3 4 Q4 6 6 7 L7 6 L9 8 L8 9 Q3 9 1 2 Z" fill="var(--white)"/></svg><span>02 9475 6302</span></li>
    <li><svg class="icon" viewBox="0 0 10 10"><rect x="0.5" y="2" width="9" height="6" fill="var(--white)"/><path d="M0.5 2 L5 5.5 L9.5 2" stroke="var(--navy)" fill="none" stroke-width=".8"/></svg><span>info@quillpixfigures.com.au</span></li>
    <li><svg class="icon" viewBox="0 0 10 10"><circle cx="5" cy="5" r="4.3" fill="none" stroke="var(--white)"/><ellipse cx="5" cy="5" rx="1.8" ry="4.3" fill="none" stroke="var(--white)"/><path d="M.7 5 H9.3" stroke="var(--white)"/></svg><span>www.quillpixfigures.com.au</span></li>
  </ul>

  <div class="photo photo--scene" role="img" aria-label="Photo of a young man leaning on a railing beside his figurine, with a lake and mountains behind"></div>
  <svg class="shape-layer" viewBox="0 0 420 595" aria-hidden="true">
    <path d="M0 329 L420 329 L420 336 C300 330 220 350 140 370 C80 388 30 410 0 430 Z" fill="var(--navy)"/>
    <path d="M0 430 C30 410 80 388 140 370 C220 350 300 330 420 336 L420 344 C300 340 220 358 145 378 C85 395 35 416 0 440 Z" fill="var(--cyan)"/>
    <path d="M0 440 C35 416 85 395 145 378 C220 358 300 340 420 344 L420 349 C300 346 222 363 148 383 C88 400 38 421 0 446 Z" fill="var(--white)"/>
  </svg>
  <div class="photo-circle photo-circle--family" role="img" aria-label="Photo of an elderly couple with a child and their figurines"></div>
</section>

</body>
</html>
```